Business Cards that are elegant and wow

I want to create and print business cards that represent my brand and stand out from the rest. We want to ensure they stay in our branding and the integrity is not lost. I am happy to look at different shapes like square etc.

It will be printed on very thick cards and will be stylish .

I want to create and print business cards that represent my brand and stand out from the rest. We want to ensure they stay in ur branding and the integrity is not lost. I am happy to look at different shapes like square etc.

Target Market(s)

real estate professionals

Industry/Entity Type

Real Estate

Contact Information for Business Card

Wren Holt
hello@bramblecovehomes.com.au
bramblecovehomes.com.au
0417 382 906 (SMS)

Colors

Designer to choose colors to be used in the design.

Requirements
Must have
• My logo
• email
• website
• Name
Nice to have
• I like the idea of printing with foil or spot gloss. You want it to stand out in a sea.
Should not have
• I would like you to stay in my colour themes. Don't change the colour of my logo

```html
<!DOCTYPE html>
<html lang="en">
<head>
<meta charset="utf-8">
<title>Bramble Cove Homes – Business Card</title>
<link rel="stylesheet" href="https://fonts.googleapis.com/css2?family=Montserrat:wght@600&family=Oswald:wght@600&family=Open+Sans:wght@400&display=swap">
<style>
  :root {
    --backdrop: #2a2a2a;
    --card-top: #222222;
    --card-bottom: #0e0e0e;
    --brand-blue: #12a7e6;
    --brand-pink: #e8197a;
    --ink-light: #f2f2f2;
    --divider: #bdbdbd;
  }
  * { margin: 0; padding: 0; box-sizing: border-box; }
  html, body {
    width: 1200px;
    height: 928px;
    overflow: hidden;
    background: var(--backdrop);
  }
  .sheet {
    position: relative;
    width: 1200px;
    height: 928px;
  }
  .card {
    position: absolute;
    left: 290px;
    width: 620px;
    height: 354px;
    overflow: hidden;
    background: linear-gradient(160deg, var(--card-top), var(--card-bottom));
    box-shadow: 0 10px 24px rgba(0, 0, 0, 0.45);
  }
  .card--front { top: 80px; }
  .card--back { top: 494px; }

  /* Front: brand name */
  .brand {
    position: absolute;
    left: 0;
    right: 0;
    top: 0;
    bottom: 40px;
    display: flex;
    align-items: center;
    justify-content: center;
    gap: 16px;
  }
  .brand__circle {
    width: 58px;
    height: 58px;
    border-radius: 50%;
    border: 5px solid var(--brand-pink);
  }
  .brand__name {
    font-family: "Montserrat", sans-serif;
    font-weight: 600;
    font-size: 30px;
    letter-spacing: 1px;
    color: var(--brand-blue);
    white-space: nowrap;
  }

  /* Back: person and contact */
  .contact-block {
    position: absolute;
    left: 0;
    right: 0;
    top: 0;
    bottom: 0;
    display: flex;
    align-items: center;
    justify-content: center;
    padding-bottom: 30px;
  }
  .person-name {
    font-family: "Oswald", sans-serif;
    font-weight: 600;
    font-size: 38px;
    line-height: 1;
    color: var(--ink-light);
    letter-spacing: 0.5px;
    white-space: nowrap;
    padding-right: 30px;
  }
  .divider {
    width: 1px;
    height: 88px;
    background: var(--divider);
    margin-right: 26px;
    flex: none;
  }
  .contact-list {
    list-style: none;
    display: flex;
    flex-direction: column;
    gap: 9px;
  }
  .contact-list li {
    display: flex;
    align-items: center;
    gap: 11px;
    font-family: "Open Sans", sans-serif;
    font-size: 14px;
    color: var(--ink-light);
    letter-spacing: 0.3px;
    white-space: nowrap;
  }
  .contact-list svg {
    width: 15px;
    height: 15px;
    flex: none;
    fill: var(--brand-pink);
  }
</style>
</head>
<body>
<main class="sheet">
  <section class="card card--front" aria-label="Card front">
    <div class="brand">
      <span class="brand__circle" aria-hidden="true"></span>
      <span class="brand__name">BRAMBLE COVE HOMES</span>
    </div>
  </section>

  <section class="card card--back" aria-label="Card back">
    <div class="contact-block">
      <h1 class="person-name">WREN HOLT</h1>
      <span class="divider" aria-hidden="true"></span>
      <ul class="contact-list">
        <li>
          <svg viewBox="0 0 16 16" aria-hidden="true"><path d="M4 1h8a1 1 0 0 1 1 1v12a1 1 0 0 1-1 1H4a1 1 0 0 1-1-1V2a1 1 0 0 1 1-1zm1 2v9h6V3zm3 10a.8.8 0 1 0 0 .01z"/></svg>
          0417 382 906
        </li>
        <li>
          <svg viewBox="0 0 16 16" aria-hidden="true"><path d="M1 3h14v1.2L8 9 1 4.2zm0 2.6 7 4.8 7-4.8V13H1z"/></svg>
          hello@bramblecovehomes.com.au
        </li>
        <li>
          <svg viewBox="0 0 16 16" aria-hidden="true"><circle cx="8" cy="8" r="7"/><path d="M1 8h14M8 1c-3 3-3 11 0 14M8 1c3 3 3 11 0 14" stroke="#111" stroke-width="1" fill="none"/></svg>
          bramblecovehomes.com.au
        </li>
      </ul>
    </div>
  </section>
</main>
</body>
</html>
```